Movie Poster - Beneath the Hollow Lantern

Documentary-film poster design.
Attached is a PDF brief with information on what is required and examples of poster designs I like.

The project is a true crime / mystery documentary film. Set in the Soviet Union in 1959.

Colors
3276b5
85abd2
ec1f27

```html
<!DOCTYPE html>
<html lang="en">
<head>
<meta charset="utf-8">
<title>Beneath the Hollow Lantern – Poster</title>
<link rel="stylesheet" href="https://fonts.googleapis.com/css2?family=Anton&family=Oswald:wght@300;400;600&family=Archivo+Narrow:wght@400&display=swap">
<style>
  :root {
    --backdrop: #d8d8d8;
    --poster-black: #000000;
    --steel-blue: #3276b5;
    --frost-blue: #85abd2;
    --blood-red: #ec1f27;
    --snow: #c9d3dc;
    --fog-mid: #56606a;
    --ink-white: #ffffff;
    --soft-grey: #d6d6d6;
  }
  * { box-sizing: border-box; margin: 0; padding: 0; }
  html, body { width: 1200px; height: 1200px; overflow: hidden; background: var(--backdrop); }
  .poster {
    position: absolute; left: 197px; top: 30px; width: 806px; height: 1140px;
    background: var(--poster-black); overflow: hidden; color: var(--ink-white);
  }
  .hero-photo {
    position: absolute; left: 0; top: 230px; width: 806px; height: 800px;
    background:
      radial-gradient(ellipse 70% 22% at 40% 80%, rgba(214,224,233,0.85) 0%, rgba(133,171,210,0.35) 55%, rgba(0,0,0,0) 100%),
      radial-gradient(ellipse 55% 30% at 75% 52%, rgba(133,171,210,0.35) 0%, rgba(50,118,181,0.12) 60%, rgba(0,0,0,0) 100%),
      radial-gradient(ellipse 75% 55% at 42% 62%, rgba(150,160,170,0.95) 0%, rgba(86,96,106,0.85) 40%, rgba(30,34,38,0.6) 75%, rgba(0,0,0,0) 100%),
      linear-gradient(180deg, #000 0%, #111418 18%, #3a4148 45%, #5a636c 70%, #1a1d20 90%, #000 100%);
  }
  .hero-photo::after {
    content: ""; position: absolute; inset: 0;
    background: linear-gradient(90deg, rgba(0,0,0,0.55) 0%, rgba(0,0,0,0) 18%, rgba(0,0,0,0) 82%, rgba(0,0,0,0.6) 100%);
  }
  .cast { position: absolute; top: 22px; left: 0; width: 100%; }
  .cast-member { position: absolute; transform: translateX(-50%); text-align: center; font-family: "Oswald", sans-serif; font-weight: 300; white-space: nowrap; }
  .cast-member .given { display: block; font-size: 14px; line-height: 16px; }
  .cast-member .surname { display: block; font-size: 30px; line-height: 34px; letter-spacing: -0.5px; }
  .title {
    position: absolute; top: 92px; left: 0; width: 100%; text-align: center;
    font-family: "Anton", sans-serif; text-transform: uppercase; line-height: 98px;
  }
  .title .line { display: block; white-space: nowrap; }
  .title .line-one { font-size: 86px; }
  .title .line-two { font-size: 92px; letter-spacing: 1px; }
  .title .accent { color: var(--blood-red); }
  .subtitle {
    position: absolute; top: 292px; left: 0; width: 100%; text-align: center;
    font-family: "Oswald", sans-serif; font-weight: 600; font-size: 28px;
  }
  .subtitle .accent { color: var(--blood-red); }
  .awards { position: absolute; top: 360px; left: 0; width: 100%; }
  .award { position: absolute; transform: translateX(-50%); width: 130px; height: 64px; }
  .award svg { position: absolute; left: 0; top: 0; }
  .award-text {
    position: absolute; left: 0; width: 100%; top: 50%; transform: translateY(-50%);
    text-align: center; font-family: "Oswald", sans-serif; font-weight: 300; font-size: 18px; line-height: 20px;
  }
  .tagline {
    position: absolute; top: 496px; right: 53px; text-align: right;
    font-family: "Oswald", sans-serif; font-weight: 600; font-size: 20px; line-height: 26.5px;
  }
  .crew-leads { position: absolute; top: 928px; left: 0; width: 100%; }
  .crew-lead { position: absolute; transform: translateX(-50%); text-align: center; white-space: nowrap; }
  .crew-lead .role { display: block; font-family: "Archivo Narrow", sans-serif; font-size: 13px; letter-spacing: 0.5px; text-transform: uppercase; color: var(--soft-grey); line-height: 14px; }
  .crew-lead .person { display: block; font-family: "Oswald", sans-serif; font-weight: 300; font-size: 28px; line-height: 30px; }
  .billing {
    position: absolute; top: 994px; left: 0; width: 100%; text-align: center; white-space: nowrap;
    font-family: "Oswald", sans-serif; font-weight: 300; font-size: 14px; line-height: 24px; text-transform: uppercase; color: var(--soft-grey);
  }
  .billing small { font-size: 7px; line-height: 7px; display: inline-block; vertical-align: middle; margin-right: 3px; }
  .release {
    position: absolute; top: 1070px; left: 0; width: 100%; text-align: center; white-space: nowrap;
    font-family: "Oswald", sans-serif; font-weight: 300; font-size: 32px; line-height: 40px; letter-spacing: 1px;
  }
  .release .gap { display: inline-block; width: 34px; }
  .website {
    position: absolute; top: 1116px; left: 0; width: 100%; text-align: center;
    font-family: "Oswald", sans-serif; font-weight: 300; font-size: 13px;
  }
</style>
</head>
<body>
<main class="poster">
  <div class="hero-photo" role="img" aria-label="Grainy black-and-white photograph of a line of hikers on skis pushing through a snowy blizzard"></div>

  <header class="cast">
    <div class="cast-member" style="left:176px"><span class="given">NAME</span><span class="surname">SURNAME</span></div>
    <div class="cast-member" style="left:313px"><span class="given">NAME</span><span class="surname">SURNAME</span></div>
    <div class="cast-member" style="left:448px"><span class="given">NAME</span><span class="surname">SURNAME</span></div>
    <div class="cast-member" style="left:610px"><span class="given">SPECIAL GUEST</span><span class="surname">NAME SURNAME</span></div>
  </header>

  <h1 class="title">
    <span class="line line-one">Beneath <span class="accent">the</span></span>
    <span class="line line-two">Hollow <span class="accent">Lantern</span></span>
  </h1>
  <p class="subtitle">The true story of the <span class="accent">Varnov Pass Incident</span></p>

  <section class="awards">
    <div class="award" style="left:206px">
      <svg width="130" height="64" viewBox="0 0 130 64" fill="none" stroke="#fff" stroke-width="3"><path d="M22 6 Q6 32 22 58"/><path d="M108 6 Q124 32 108 58"/></svg>
      <div class="award-text">BEST<br>FEATURE<br>FILM</div>
    </div>
    <div class="award" style="left:410px">
      <svg width="130" height="64" viewBox="0 0 130 64" fill="none" stroke="#fff" stroke-width="3"><path d="M22 6 Q6 32 22 58"/><path d="M108 6 Q124 32 108 58"/></svg>
      <div class="award-text">BEST<br>DIRECTOR</div>
    </div>
    <div class="award" style="left:610px">
      <svg width="130" height="64" viewBox="0 0 130 64" fill="none" stroke="#fff" stroke-width="3"><path d="M22 6 Q6 32 22 58"/><path d="M108 6 Q124 32 108 58"/></svg>
      <div class="award-text">BEST<br>ACTRESS</div>
    </div>
  </section>

  <p class="tagline">Nine dead hikers<br>Sixty years of secrets<br>Russia’s greatest mystery<br>uncovered</p>

  <section class="crew-leads">
    <div class="crew-lead" style="left:206px"><span class="role">Directed by</span><span class="person">DIRECTOR</span></div>
    <div class="crew-lead" style="left:410px"><span class="role">Screenplay by</span><span class="person">WRITER</span></div>
    <div class="crew-lead" style="left:610px"><span class="role">Story by</span><span class="person">WRITER</span></div>
  </section>

  <div class="billing">
    Northfield Pictures presents a Northfield production in association with Studio Kestrel actor name actor name "Movie Title"<br>
    <small>CASTING<br>BY</small>Casting crew &nbsp; <small>MUSIC<br>BY</small>Composer &nbsp; <small>COSTUME<br>DESIGNER</small>Costume designer &nbsp; <small>EDITED<br>BY</small>Editor &nbsp; <small>PRODUCTION<br>DESIGNER</small>Production designer &nbsp; <small>PRODUCED<br>BY</small>Producer<br>
    <small>DIRECTOR OF<br>PHOTOGRAPHY</small>Director of photography &nbsp; <small>CO-EXECUTIVE<br>PRODUCER</small>Co-executive producer &nbsp; <small>EXECUTIVE<br>PRODUCER</small>Executive producer
  </div>

  <p class="release">COMING SOON<span class="gap"></span>MONTH YEAR</p>
  <p class="website">WWW.HOLLOWLANTERNFILM.COM</p>
</main>
</body>
</html>
```